Online-Marketing Material für Recruiting-Plattform
Zielgruppe
Recruiting-Plattform für Physiotherapeuten. Wir sind Vermittler.
Aufgabenstellung
Ich benötige ein 2er Set aus Social-Media-Templates, das wir als Basis für Recruiting-Ads nutzen können.
Variante 1: (1080 x 1350) mit jeweils 285 Pixel Safe Space oben und unten (hier keine wichtigen Elemente).
Wichtig: Es handelt sich um ein Template. Daher muss es mit verschiedenen Elementen und Fotos funktionieren.
Die Elemente werden später durch variable Inhalte gesetzt. Ziel ist es, ein möglichst flexibles Format zu schaffen,
das mit unterschiedlichen Inhalten funktioniert.
Bitte orientiere dich am Grunddesign der Website therapunkt.de
Elemente und zugehörige Beispiele sind
1. Foto in querformat | Beispiel als Download)
2. Jobtitel als Headline | (Physiotherapeut (m/w/d)
3. Subtitle | Werde Teil eines wachsenden Teams
4. Arbeitszeitmodell | Vollzeit, Teilzeit
3. Ort | Hannover
4. 3 x Highlights | 1. Betriebliche Krankenversicherung 2. Tretlux 3. Gehalt bis zu 4.500 EUR
(Die Highlight variieren thematisch, daher hier bitte nur mit thematisch-neutralen Icons arbeiten.
5. Logo des Arbeitgebers (lusen) auf weiß
Variante 2 mit Foto in hochformat

```html
<!DOCTYPE html>
<html lang="de">
<head>
<meta charset="utf-8">
<title>lusen – Recruiting Templates</title>
<link href="https://fonts.googleapis.com/css2?family=Mulish:wght@400;900&family=Nunito:ital,wght@1,800&family=Roboto:wght@500&display=swap" rel="stylesheet">
<style>
  :root{
    --stage:#275682;
    --brand-blue:#5b91c1;
    --brand-pink:#d85b84;
    --paper:#ffffff;
    --paper-grey:#f4f4f4;
    --ink:#111111;
    --pin:#d22b3a;
    --photo-therapy-a:#dfe3e6;
    --photo-therapy-b:#8a98a8;
    --photo-room-a:#f3ead2;
    --photo-room-b:#4a4d52;
  }
  *{box-sizing:border-box;margin:0;padding:0}
  html,body{width:1200px;height:960px;overflow:hidden;background:var(--stage)}
  .stage{position:relative;width:1200px;height:960px}
  .template{position:absolute;top:156px;width:518px;height:648px;background:var(--paper);overflow:hidden;box-shadow:0 4px 18px rgba(0,0,0,.18)}
  .template--landscape{left:65px}
  .template--portrait{left:617px}
  .shapes{position:absolute;inset:0;width:518px;height:648px}
  .subtitle{position:absolute;font-family:"Mulish",sans-serif;font-size:27px;line-height:30px;color:var(--ink);letter-spacing:.2px}
  .subtitle strong{font-weight:900;display:block}
  .job-title{position:absolute;font-family:"Nunito",sans-serif;font-style:italic;font-weight:800;font-size:22px;color:var(--paper);white-space:nowrap;transform:rotate(-2deg);transform-origin:left bottom}
  .job-title small{font-size:14px}
  .work-model{position:absolute;font-family:"Nunito",sans-serif;font-style:italic;font-weight:800;font-size:16.5px;color:var(--paper);white-space:nowrap;transform:rotate(-2deg);transform-origin:left bottom}
  .highlights{position:absolute;list-style:none;font-family:"Roboto",sans-serif;font-weight:500;font-size:16.5px;line-height:21px;color:var(--ink)}
  .highlights li{position:relative;padding-left:20px;margin-bottom:5px}
  .highlights svg{position:absolute;left:0;top:2px;width:16px;height:16px}
  .location{position:absolute;display:flex;align-items:center;gap:6px;font-family:"Roboto",sans-serif;font-weight:500;color:var(--ink)}
  .location svg{width:13px;height:17px}
  .photo-frame{position:absolute;background:var(--paper);padding:5px;box-shadow:0 6px 10px rgba(0,0,0,.25)}
  .photo{width:100%;height:100%}
  .photo--therapy{background:linear-gradient(120deg,var(--photo-therapy-a) 0%,#f4f5f6 45%,var(--photo-therapy-b) 100%)}
  .photo--room{background:linear-gradient(160deg,var(--photo-room-a) 0%,#fbf6e6 45%,var(--photo-room-b) 100%)}
  .brand{position:absolute;display:flex;align-items:center;gap:6px;font-family:"Mulish",sans-serif;font-weight:400;color:var(--paper)}
  .brand-dot{border-radius:50%;background:var(--paper)}
  .brand-tab{position:absolute;left:0;top:14px;width:128px;height:52px;background:var(--brand-pink)}
</style>
</head>
<body>
<div class="stage">

  <!-- Template 1: landscape photo -->
  <section class="template template--landscape">
    <svg class="shapes" viewBox="0 0 518 648" aria-hidden="true">
      <polygon points="323,0 518,0 518,326 342,278" fill="var(--brand-blue)"/>
      <polygon points="0,463 518,444 518,648 0,648" fill="var(--paper-grey)"/>
      <polygon points="0,240 321,228 321,265 0,276" fill="var(--brand-pink)"/>
      <polygon points="0,276 169,270 169,300 0,308" fill="var(--brand-blue)"/>
    </svg>

    <div class="brand" style="left:372px;top:170px;font-size:38px">
      <span>lusen</span><span class="brand-dot" style="width:18px;height:18px"></span>
    </div>

    <h2 class="subtitle" style="left:33px;top:158px">Werde Teil eines<strong>wachsenden Teams</strong></h2>
    <p class="job-title" style="left:36px;top:235px">Physiotherapeut (m/w/d)</p>
    <p class="work-model" style="left:34px;top:280px">Vollzeit, Teilzeit</p>

    <ul class="highlights" style="left:33px;top:318px">
      <li><svg viewBox="0 0 16 16"><path d="M8 14 2 8.2A3.4 3.4 0 0 1 8 3.6a3.4 3.4 0 0 1 6 4.6Z" fill="var(--brand-pink)"/><circle cx="11.5" cy="11" r="3.4" fill="var(--paper)"/><path d="m9.8 11 1.2 1.2 2.1-2.3" stroke="var(--brand-pink)" stroke-width="1.3" fill="none"/></svg>Betriebliche<br>Krankenversicherung</li>
      <li><svg viewBox="0 0 16 16"><rect x="1" y="4.5" width="14" height="10" rx="1.5" fill="var(--brand-pink)"/><path d="M5.5 4.5V3h5v1.5" stroke="var(--brand-pink)" stroke-width="1.5" fill="none"/><rect x="1" y="8.6" width="14" height="1.2" fill="var(--paper)"/></svg>Tretlux</li>
      <li><svg viewBox="0 0 16 16"><path d="M5.5 1h5L9 4H7Z" fill="var(--brand-pink)"/><path d="M6.5 4.5h3C13 7 14.5 11 13 13.5c-.8 1.3-2.5 1.5-5 1.5s-4.2-.2-5-1.5C1.5 11 3 7 6.5 4.5Z" fill="var(--brand-pink)"/><text x="8" y="12.8" font-size="6.5" text-anchor="middle" fill="var(--paper)" font-family="Roboto,sans-serif">€</text></svg>Gehalt bis zu<br>4.500 EUR</li>
    </ul>

    <div class="location" style="left:33px;top:479px;font-size:12.5px">
      <svg viewBox="0 0 13 17"><path d="M6.5 17S0 10 0 6.5a6.5 6.5 0 0 1 13 0C13 10 6.5 17 6.5 17Z" fill="var(--pin)"/><circle cx="6.5" cy="6.3" r="3" fill="var(--paper)"/></svg>
      <span>Ort: Hannover</span>
    </div>

    <div class="photo-frame" style="left:227px;top:280px;width:272px;height:200px;transform:rotate(-1.8deg)">
      <div class="photo photo--therapy" role="img" aria-label="Foto: Physiotherapeutin behandelt das Bein eines Patienten auf einer Liege in einem hellen Raum"></div>
    </div>
  </section>

  <!-- Template 2: portrait photo -->
  <section class="template template--portrait">
    <svg class="shapes" viewBox="0 0 518 648" aria-hidden="true">
      <polygon points="0,0 113,0 141,648 0,648" fill="var(--brand-blue)"/>
      <polygon points="141,470 518,449 518,648 141,648" fill="var(--paper-grey)"/>
      <polygon points="233,250 518,240 518,276 233,287" fill="var(--brand-pink)"/>
      <polygon points="236,288 397,282 397,313 236,320" fill="var(--brand-blue)"/>
    </svg>

    <div class="photo-frame" style="left:-12px;top:166px;width:256px;height:333px;transform:rotate(-2deg)">
      <div class="photo photo--room" role="img" aria-label="Foto: heller Behandlungsraum mit Therapieliege, Fenster und Pflanze"></div>
      <div class="brand-tab"></div>
      <div class="brand" style="left:28px;top:26px;font-size:22px">
        <span>lusen</span><span class="brand-dot" style="width:11px;height:11px"></span>
      </div>
    </div>

    <h2 class="subtitle" style="left:245px;top:174px">Werde Teil eines<strong>wachsenden Teams</strong></h2>
    <p class="job-title" style="left:261px;top:244px">Physiotherapeut <small>(m/w/d)</small></p>
    <p class="work-model" style="left:260px;top:292px">Vollzeit, Teilzeit</p>

    <ul class="highlights" style="left:266px;top:325px">
      <li><svg viewBox="0 0 16 16"><path d="M8 14 2 8.2A3.4 3.4 0 0 1 8 3.6a3.4 3.4 0 0 1 6 4.6Z" fill="var(--brand-pink)"/><circle cx="11.5" cy="11" r="3.4" fill="var(--paper)"/><path d="m9.8 11 1.2 1.2 2.1-2.3" stroke="var(--brand-pink)" stroke-width="1.3" fill="none"/></svg>Betriebliche<br>Krankenversicherung</li>
      <li><svg viewBox="0 0 16 16"><rect x="1" y="4.5" width="14" height="10" rx="1.5" fill="var(--brand-pink)"/><path d="M5.5 4.5V3h5v1.5" stroke="var(--brand-pink)" stroke-width="1.5" fill="none"/><rect x="1" y="8.6" width="14" height="1.2" fill="var(--paper)"/></svg>Tretlux</li>
      <li><svg viewBox="0 0 16 16"><path d="M5.5 1h5L9 4H7Z" fill="var(--brand-pink)"/><path d="M6.5 4.5h3C13 7 14.5 11 13 13.5c-.8 1.3-2.5 1.5-5 1.5s-4.2-.2-5-1.5C1.5 11 3 7 6.5 4.5Z" fill="var(--brand-pink)"/><text x="8" y="12.8" font-size="6.5" text-anchor="middle" fill="var(--paper)" font-family="Roboto,sans-serif">€</text></svg>Gehalt bis zu<br>4.500 EUR</li>
    </ul>

    <div class="location" style="right:22px;top:472px;font-size:14px">
      <svg viewBox="0 0 13 17"><path d="M6.5 17S0 10 0 6.5a6.5 6.5 0 0 1 13 0C13 10 6.5 17 6.5 17Z" fill="var(--pin)"/><circle cx="6.5" cy="6.3" r="3" fill="var(--paper)"/></svg>
      <span>Ort: Hannover</span>
    </div>
  </section>

</div>
</body>
</html>
```